House Cleaning Website - Maid Services

Logo, landing page design with contact form - coded MUST BE MOBILE FRIENDLY

Cleaning business - maid service - i've added a few example websites

Clean, Smart Website Design that is built for getting leads

CONTENT FOR HOME PAGE -

Cleaning Seminole County Homes For Over 12 Years

Rosetta Cleans

* Trusted by your neighbors for more than a decade
* Affordable and flexible to accommodate your needs
* 200% Money Back Guarantee
* Up to 20% Discount on Continued Cleanings
* Same Day Cleanings

My Clients Are Happy
"Rosetta has been cleaning my home for the past 3 1/2 years and I couldn't be happier with her. I trust her with cleaning my home while I'm out of town and recommend her to my friends."

Target Market(s)

people looking for house cleaning

Industry/Entity Type

Cleaning Service

Contact Information for Business Card

Rosetta Cleans -
#321-555-0187
200% Guarantee
on back of card - $25 Referral Fee

Logo Text

Rosetta Cleans

Coding

Coded - Design and coding required

Number of Pages Required

3 page

Requirements
Must have
• 4 links in top toolbar - services, contact, free estimate and about
• *contact will be a popup form to contact
• *services will be a graphic similar to the one on this page ... https://www.brightbroomcrew.com/maid-services/
• *free estimate link will be a page with same questions as
• Must have landing page concept - I will be advertising to get people to submit their information...
• 1. Must have a "Request FREE Estimate" button that pops up a box for them to submit their information - name, number, email. Once they submit this information, they will be taken to a 2nd form to complete their details - If they dont complete the 2nd part I still receive the 1st part to call. The 2nd part will have same questions ashttps://www.tidyhenwick.com/local-house-cleaning/fl/west-miami/request-a-cleaning.aspx?cpgnId=FE0CA3B4-3A4C-4D9C-9B11-E69492B42092&scid=3554195&cid=2303288&tc=17072613580054989&rl_key=a0563857ec931d2a952e39d66a08939d&kw=77903:7716&pub_cr_id=200261568213&dynamic_proxy=1&primary_serv=www.tidyhenwick.com&rl_track_landing_pages=1
• 2. Must have pricing like https://www.brightbroomcrew.com/ 1 bedroom through 6 bedroom pricing base pricing graphic.
• 2.Must have a 200% satisfaction guarantee graphic
• 3.Must have phone number visible
• 4. graphics offering - 1st deep clean $25 Off - 10% Off Bi Weekly Cleanings - 20% Off Weekly Cleanings
• I like the clean look of this website https://www.pearlofsuds.com/ BUT want a more compact website like https://www.brightbroomcrew.com/
• Popup for when the try and x out saying Book Now And Receive $20 Off 1st Cleaning

```html
<!DOCTYPE html>
<html lang="en">
<head>
<meta charset="utf-8">
<title>Rosetta Cleans – House Cleaning Maid Services</title>
<link rel="stylesheet" href="https://fonts.googleapis.com/css2?family=Lato:ital,wght@0,400;0,700;0,900;1,400&display=swap">
<style>
  :root{
    --blue:#1d4f9c;
    --blue-dark:#173f7e;
    --gold:#f2b92b;
    --gold-dark:#e3a81a;
    --ink:#333;
    --muted:#555;
    --light:#f7f7f7;
    --rule:#e2e2e2;
    --footer:#2e3135;
    --footer-base:#222427;
  }
  *{box-sizing:border-box;margin:0;padding:0}
  html,body{width:926px;height:1200px;overflow:hidden;background:#fff}
  body{font-family:"Lato",sans-serif;color:var(--ink);position:relative}

  /* header */
  .site-header{position:absolute;left:0;top:0;width:926px;height:90px;background:#fff}
  .brand{position:absolute;left:101px;top:22px}
  .brand-name{font-size:23px;font-weight:900;color:var(--blue);letter-spacing:-.3px;line-height:1}
  .brand-tag{font-size:10px;color:#444;letter-spacing:.8px;margin-top:11px}
  .phone-icon{position:absolute;left:554px;top:18px}
  .phone-label{position:absolute;left:593px;top:21px;font-size:9px;color:#555}
  .phone-number{position:absolute;left:593px;top:33px;font-size:12px;font-weight:700;color:var(--blue)}
  .btn-outline{position:absolute;border:1px solid var(--gold);color:var(--gold-dark);font-size:11.5px;display:flex;align-items:center;justify-content:center;background:transparent}
  .estimate-btn{left:688px;top:18px;width:136px;height:31px}
  .main-nav{position:absolute;top:65px;left:0;font-size:11px;color:#222}
  .main-nav span{position:absolute;white-space:nowrap}
  .main-nav .active{color:var(--blue)}
  .nav-underline{position:absolute;left:378px;top:87px;width:41px;height:3px;background:var(--blue)}

  /* hero */
  .hero{position:absolute;left:0;top:90px;width:926px;height:360px;
    background:linear-gradient(100deg,#6f8a34 0%,#c7b58c 25%,#e6dfd6 45%,#c9b8a8 62%,#b64a3a 80%,#3c6e3a 100%)}
  .hero-shade{position:absolute;inset:0;background:linear-gradient(90deg,rgba(0,0,0,0) 40%,rgba(0,0,0,.15) 100%)}
  .hero-title{position:absolute;right:100px;top:164px;text-align:right;color:#fff;font-weight:700;font-size:29px;line-height:42px;text-shadow:0 2px 4px rgba(0,0,0,.35)}
  .slider-dots{position:absolute;left:0;top:315px}
  .slider-dots i{position:absolute;width:9px;height:9px;border-radius:50%;border:1.5px solid #fff}
  .slider-dots i.on{background:var(--gold);border-color:var(--gold)}

  .price-panel{position:absolute;left:102px;top:90px;width:160px;height:360px;background:rgba(20,20,20,.88);color:#fff}
  .price-head{height:46px;background:var(--gold);font-size:18px;font-weight:700;padding:13px 0 0 13px}
  .price-row{position:absolute;left:13px;width:137px;height:31px;border-bottom:1px solid rgba(255,255,255,.18);display:flex;justify-content:space-between;align-items:center}
  .price-row .room{font-size:9.5px}
  .price-row .amt{font-size:13px;font-weight:700}
  .book-btn{left:13px;top:250px;width:135px;height:31px}
  .accept-rule{position:absolute;left:13px;top:300px;width:137px;height:1px;background:rgba(255,255,255,.18)}
  .accept-label{position:absolute;left:0;width:160px;top:312px;text-align:center;font-size:9.5px}
  .cards{position:absolute;left:23px;top:332px;display:flex;gap:4px}
  .cards span{width:26px;height:16px;background:#fff;border-radius:1px}

  /* features */
  .features{position:absolute;left:0;top:450px;width:926px;height:314px;background:var(--light);border-bottom:1px solid var(--rule)}
  .video-card{position:absolute;left:102px;top:44px;width:339px;height:214px;background:#fff;border:1px solid #e0e0e0;box-shadow:0 1px 3px rgba(0,0,0,.06)}
  .video-still{position:absolute;left:4px;top:5px;width:330px;height:182px;background:linear-gradient(110deg,#f1ece4 0%,#e8dfd2 40%,#d9cbb8 70%,#c9b9a3 100%)}
  .play{position:absolute;left:146px;top:76px}
  .video-bar{position:absolute;left:4px;top:187px;width:330px;height:21px;background:linear-gradient(#fafafa,#e9e9e9);font-size:5.5px;color:#444}
  .features-title{position:absolute;left:486px;top:37px;font-size:22px;font-weight:400;color:#333}
  .features-lede{position:absolute;left:486px;top:71px;font-size:8.4px;color:#444}
  .feature-list{position:absolute;left:486px;top:92px;list-style:none}
  .feature-list li{height:24.8px;display:flex;align-items:center;font-size:9.4px;color:#555}
  .feature-list svg{margin-right:12px}
  .contact-btn{left:486px;top:228px;width:80px;height:31px}

  /* offers */
  .offer{position:absolute;left:102px;width:348px;height:43px}
  .offer-tag{position:absolute;left:0;top:0;width:89px;height:43px;background:var(--gold);color:#fff;font-size:16px;display:flex;align-items:center;justify-content:center}
  .offer-arrow{position:absolute;left:89px;top:0}
  .offer-text{position:absolute;left:110px;top:8px;color:#fff}
  .offer-text b{display:block;font-size:12px;font-weight:400}
  .offer-text small{display:block;font-size:7.2px;margin-top:3px}

  .testimonials-title{position:absolute;left:483px;top:806px;font-size:16px;font-weight:400;color:#333}
  .quote-box{position:absolute;left:483px;top:834px;width:341px;height:104px;background:#fff;border:1px solid #ddd;box-shadow:0 1px 3px rgba(0,0,0,.06)}
  .quote-mark{position:absolute;left:16px;top:10px;font-size:16px;color:#555;font-style:italic}
  .quote-text{position:absolute;left:15px;top:26px;width:314px;font-size:9.2px;font-style:italic;color:#444;line-height:18.4px;text-indent:8px}
  .quote-name{position:absolute;right:20px;top:81px;font-size:9px;color:var(--blue)}
  .quote-curl{position:absolute;left:796px;top:938px}

  /* footer */
  .site-footer{position:absolute;left:0;top:1006px;width:926px;height:154px;background:var(--footer);color:#ddd}
  .footer-brand{position:absolute;left:101px;top:60px}
  .footer-brand .brand-name{color:#9a9ea3}
  .footer-brand .brand-tag{color:#9a9ea3}
  .footer-col h4{position:absolute;font-weight:400;font-size:12px;color:#fff;top:25px}
  .quick-links{position:absolute;left:303px;top:55px;list-style:none;font-size:8.6px;color:#d0d0d0}
  .quick-links li{height:16px}
  .guarantee-seal{position:absolute;left:420px;top:54px}
  .email-field{position:absolute;left:550px;top:52px;width:148px;height:32px;border:1px solid #ccc;font-size:8.6px;color:#ccc;padding:10px 0 0 12px}
  .subscribe-btn{left:550px;top:90px;width:68px;height:32px}
  .social{position:absolute;left:760px;list-style:none}
  .social li{position:absolute;left:0;display:flex;align-items:center;font-size:8.6px;color:#ddd;white-space:nowrap}
  .social li i{width:16px;height:16px;background:#fff;border-radius:2px;margin-right:8px}
  .footer-base{position:absolute;left:0;top:1160px;width:926px;height:40px;background:var(--footer-base);color:#aaa;font-size:8.6px;text-align:center;line-height:40px;padding-right:5px}
</style>
</head>
<body>

<header class="site-header">
  <div class="brand">
    <div class="brand-name">Rosetta Cleans</div>
    <div class="brand-tag">House Cleaning Maid Services</div>
  </div>

  <svg class="phone-icon" width="32" height="32" viewBox="0 0 32 32" aria-hidden="true">
    <circle cx="16" cy="16" r="14.5" fill="none" stroke="#1d4f9c" stroke-width="2"/>
    <path d="M11 9.5c1-.8 2-.6 2.6.3l1.4 2.3c.4.7.2 1.5-.4 2l-1 .8c.8 1.8 2.1 3.2 3.8 4.1l.9-1c.5-.6 1.3-.7 2-.3l2.3 1.4c.9.6 1 1.7.2 2.6l-1.1 1.2c-3.4 1.3-11.1-6.3-10.2-10.7z" fill="#1d4f9c"/>
  </svg>
  <div class="phone-label">Phone :</div>
  <div class="phone-number">+345-555-0142</div>
  <div class="btn-outline estimate-btn">Request FREE Estimate</div>

  <nav class="main-nav">
    <span class="active" style="left:385px">Home</span>
    <span style="left:458px">Services</span>
    <span style="left:541px">Contact</span>
    <span style="left:622px">Free Estimate</span>
    <span style="left:730px">About</span>
    <svg style="position:absolute;left:798px;top:1px" width="13" height="13" viewBox="0 0 13 13" aria-hidden="true">
      <circle cx="5.5" cy="5.5" r="4.5" fill="none" stroke="#444" stroke-width="1.2"/>
      <line x1="8.8" y1="8.8" x2="12.3" y2="12.3" stroke="#444" stroke-width="1.2"/>
    </svg>
  </nav>
  <div class="nav-underline"></div>
</header>

<section class="hero" role="img" aria-label="Gloved hands wiping a white table with a cloth and spray bottle beside potted flowers">
  <div class="hero-shade"></div>
  <h1 class="hero-title">Cleaning Seminole County Homes<br>For Over 12 Years</h1>
  <div class="slider-dots">
    <i class="on" style="left:766px"></i><i style="left:791px"></i><i style="left:816px"></i>
  </div>
</section>

<aside class="price-panel">
  <div class="price-head">Prices Start At</div>
  <div class="price-row" style="top:47px"><span class="room">One Bedroom Home</span><span class="amt">$85</span></div>
  <div class="price-row" style="top:78px"><span class="room">Two Bedroom Home</span><span class="amt">$90</span></div>
  <div class="price-row" style="top:109px"><span class="room">Three Bedroom Home</span><span class="amt">$105</span></div>
  <div class="price-row" style="top:140px"><span class="room">Four Bedroom Home</span><span class="amt">$120</span></div>
  <div class="price-row" style="top:171px"><span class="room">Five Bedroom Home</span><span class="amt">$150</span></div>
  <div class="price-row" style="top:202px"><span class="room">Six Bedroom Home</span><span class="amt">$200</span></div>
  <div class="btn-outline book-btn">Book in 60 Seconds</div>
  <div class="accept-rule"></div>
  <div class="accept-label">We Accept</div>
  <div class="cards"><span></span><span></span><span></span><span></span></div>
</aside>

<section class="features">
  <div class="video-card">
    <div class="video-still" role="img" aria-label="Two cleaners in green aprons wiping a table and mopping a living room floor"></div>
    <svg class="play" width="40" height="40" viewBox="0 0 40 40" aria-hidden="true">
      <circle cx="20" cy="20" r="18" fill="rgba(0,0,0,.55)" stroke="#fff" stroke-width="2"/>
      <path d="M16 12l12 8-12 8z" fill="none" stroke="#fff" stroke-width="2" stroke-linejoin="round"/>
    </svg>
    <div class="video-bar">
      <svg style="position:absolute;left:7px;top:7px" width="6" height="7" viewBox="0 0 6 7" aria-hidden="true"><path d="M0 0l6 3.5L0 7z" fill="#222"/></svg>
      <span style="position:absolute;left:31px;top:7px">10:00/05:03</span>
      <span style="position:absolute;left:84px;top:9px;width:151px;height:2px;background:#444"></span>
      <span style="position:absolute;left:84px;top:9px;width:70px;height:2px;background:#e5432b"></span>
      <svg style="position:absolute;left:282px;top:6px" width="10" height="8" viewBox="0 0 10 8" aria-hidden="true"><path d="M0 2.5h2l3-2.5v8l-3-2.5H0z" fill="#222"/><path d="M7 2c1 1 1 3 0 4M8.5 1c1.6 1.6 1.6 4.4 0 6" stroke="#222" fill="none" stroke-width=".8"/></svg>
      <span style="position:absolute;left:295px;top:9px;width:30px;height:2px;background:#e5432b"></span>
    </div>
  </div>

  <h2 class="features-title">Rosetta Cleans Features</h2>
  <p class="features-lede">Lorem ipsum dolor sit amet, consectetur adipiscing elit, sed do eiusmod tempor incididunt</p>
  <ul class="feature-list">
    <li><svg width="17" height="17" viewBox="0 0 20 20" aria-hidden="true"><path d="M10 0l1.6 8.4L20 10l-8.4 1.6L10 20l-1.6-8.4L0 10l8.4-1.6z" fill="#f2b92b"/></svg>Trusted by your neighbors for more than a decade</li>
    <li><svg width="17" height="17" viewBox="0 0 20 20" aria-hidden="true"><path d="M10 0l1.6 8.4L20 10l-8.4 1.6L10 20l-1.6-8.4L0 10l8.4-1.6z" fill="#f2b92b"/></svg>Affordable and flexible to accommodate your needs</li>
    <li><svg width="17" height="17" viewBox="0 0 20 20" aria-hidden="true"><path d="M10 0l1.6 8.4L20 10l-8.4 1.6L10 20l-1.6-8.4L0 10l8.4-1.6z" fill="#f2b92b"/></svg>200% Money Back Guarantee</li>
    <li><svg width="17" height="17" viewBox="0 0 20 20" aria-hidden="true"><path d="M10 0l1.6 8.4L20 10l-8.4 1.6L10 20l-1.6-8.4L0 10l8.4-1.6z" fill="#f2b92b"/></svg>Up to 20% Discount on Continued Cleanings</li>
    <li><svg width="17" height="17" viewBox="0 0 20 20" aria-hidden="true"><path d="M10 0l1.6 8.4L20 10l-8.4 1.6L10 20l-1.6-8.4L0 10l8.4-1.6z" fill="#f2b92b"/></svg>Same Day Cleanings</li>
  </ul>
  <div class="btn-outline contact-btn">Contact Us</div>
</section>

<section class="offers">
  <div class="offer" style="top:812px">
    <div class="offer-tag">$25 Off</div>
    <svg class="offer-arrow" width="260" height="43" viewBox="0 0 260 43" aria-hidden="true"><defs><linearGradient id="rib" x1="0" y1="0" x2="1" y2="0"><stop offset="0" stop-color="#1d4f9c"/><stop offset="1" stop-color="#2a63b8"/></linearGradient></defs><path d="M0 0h237l22 21.5-22 21.5H0z" fill="url(#rib)"/></svg>
    <div class="offer-text"><b>1st Deep Clean</b><small>Lorem ipsum dolor sit amet, consectetur adipiscing elit...</small></div>
  </div>
  <div class="offer" style="top:862px">
    <div class="offer-tag">10% Off</div>
    <svg class="offer-arrow" width="260" height="43" viewBox="0 0 260 43" aria-hidden="true"><path d="M0 0h237l22 21.5-22 21.5H0z" fill="url(#rib)"/></svg>
    <div class="offer-text"><b>Bi Weekly Cleanings</b><small>Lorem ipsum dolor sit amet, consectetur adipiscing elit...</small></div>
  </div>
  <div class="offer" style="top:911px">
    <div class="offer-tag">20% Off</div>
    <svg class="offer-arrow" width="260" height="43" viewBox="0 0 260 43" aria-hidden="true"><path d="M0 0h237l22 21.5-22 21.5H0z" fill="url(#rib)"/></svg>
    <div class="offer-text"><b>Weekly Cleanings</b><small>Lorem ipsum dolor sit amet, consectetur adipiscing elit...</small></div>
  </div>

  <h3 class="testimonials-title">Testimonials</h3>
  <blockquote class="quote-box">
    <span class="quote-mark">“</span>
    <p class="quote-text">Rosetta has been cleaning my home for the past 3 1/2 years and I couldn't be happier with her. I trust her with cleaning my home while I'm out of town and recommend her to my friends</p>
    <span class="quote-name">-Client Name</span>
  </blockquote>
  <svg class="quote-curl" width="28" height="20" viewBox="0 0 28 20" aria-hidden="true"><path d="M0 0h28L2 20z" fill="#ddd"/></svg>
</section>

<footer class="site-footer">
  <div class="footer-brand">
    <div class="brand-name">Rosetta Cleans</div>
    <div class="brand-tag">House Cleaning Maid Services</div>
  </div>
  <div class="footer-col"><h4 style="left:303px">Quick Links</h4></div>
  <ul class="quick-links"><li>Home</li><li>Services</li><li>Contact</li><li>Free Estimate</li><li>About</li></ul>

  <div class="footer-col"><h4 style="left:427px">Guarantee</h4></div>
  <svg class="guarantee-seal" width="68" height="68" viewBox="0 0 68 68" aria-label="Satisfaction guarantee seal" role="img">
    <circle cx="34" cy="34" r="33" fill="#e3a81a"/>
    <circle cx="34" cy="34" r="25" fill="#f2c64a"/>
  </svg>

  <div class="footer-col"><h4 style="left:550px">Newsletter</h4></div>
  <div class="email-field">E-mail Address</div>
  <div class="btn-outline subscribe-btn">Subscribe</div>

  <div class="footer-col"><h4 style="left:760px">Follow Us</h4></div>
  <ul class="social">
    <li style="top:60px"><i></i>Friendbook</li>
    <li style="top:88px"><i></i>Chirper</li>
    <li style="top:116px"><i></i>Circleplus</li>
  </ul>
</footer>
<div class="footer-base">Copyrights © 2017 , Rosetta Cleans | All rights reserved.</div>

</body>
</html>
```